Hydraulics Company Business Card Design

Modern business card design for a hydraulics company.
Our company colours are - black, orange and white.
I would like the following contact details included-
Name
Position
Phone number
Email
Website
Street Address

I have attached our company logo.
I would like the back of the card white.

Thank you.

```html
<!DOCTYPE html>
<html lang="en">
<head>
<meta charset="utf-8">
<title>Ridgeway Hydraulics – Business Card</title>
<link rel="stylesheet" href="https://fonts.googleapis.com/css2?family=Montserrat:wght@700&family=Open+Sans:wght@400;600&display=swap">
<style>
  :root {
    --canvas: #333333;
    --white: #ffffff;
    --orange: #f7a12a;
    --black: #111111;
    --grey: #555555;
  }
  * { box-sizing: border-box; margin: 0; padding: 0; }
  html, body { width: 1200px; height: 780px; overflow: hidden; }
  body {
    background: var(--canvas);
    display: flex;
    align-items: center;
    justify-content: center;
    gap: 40px;
    font-family: "Open Sans", Arial, sans-serif;
  }
  .card {
    position: relative;
    width: 540px;
    height: 309px;
    border-radius: 24px;
    background: var(--white);
    overflow: hidden;
  }
  .brand {
    font-family: "Montserrat", Arial, sans-serif;
    font-weight: 700;
    color: var(--orange);
    line-height: 1.05;
  }
  .card-back .brand {
    position: absolute;
    inset: 0;
    display: flex;
    flex-direction: column;
    align-items: center;
    justify-content: center;
    font-size: 44px;
    text-align: center;
  }
  .card-front .brand {
    position: absolute;
    right: 40px;
    top: 30px;
    font-size: 28px;
    text-align: right;
  }
  .band { position: absolute; inset: 0; }
  .person {
    position: absolute;
    left: 38px;
    top: 128px;
  }
  .person-name {
    font-family: "Montserrat", Arial, sans-serif;
    font-weight: 700;
    font-size: 19px;
    color: var(--orange);
    letter-spacing: 0.5px;
  }
  .person-role {
    font-size: 14px;
    color: var(--grey);
    margin-top: 1px;
  }
  .contacts {
    position: absolute;
    left: 44px;
    bottom: 16px;
    list-style: none;
    color: var(--white);
    font-size: 13.5px;
  }
  .contacts li {
    display: flex;
    align-items: center;
    gap: 8px;
    line-height: 22px;
  }
  .contacts svg { width: 13px; height: 13px; flex: none; }
  .address {
    position: absolute;
    right: 30px;
    top: 192px;
    text-align: right;
    color: var(--white);
    font-size: 13px;
    line-height: 18px;
  }
</style>
</head>
<body>

  <section class="card card-back" aria-label="Card back">
    <div class="brand"><span>Ridgeway</span><span>Hydraulics</span></div>
  </section>

  <section class="card card-front" aria-label="Card front">
    <div class="brand">Ridgeway<br>Hydraulics</div>

    <svg class="band" viewBox="0 0 540 309" aria-hidden="true">
      <path d="M0 220 L300 194 C312 191 314 204 326 204 C338 204 340 194 352 192 L540 142 V309 H0 Z"
            fill="var(--black)"/>
      <path d="M0 212 L300 186 C312 183 314 196 326 196 C338 196 340 186 352 184 L540 134"
            fill="none" stroke="var(--orange)" stroke-width="4"/>
    </svg>

    <div class="person">
      <p class="person-name">DANIEL MARSH</p>
      <p class="person-role">Managing Director</p>
    </div>

    <ul class="contacts">
      <li>
        <svg viewBox="0 0 16 16"><circle cx="8" cy="8" r="8" fill="var(--orange)"/><path d="M5 4.5l1.6-.6 1 2.2-1 .8a5 5 0 0 0 2.5 2.5l.8-1 2.2 1-.6 1.6C8 11.5 4.5 8 5 4.5z" fill="var(--black)"/></svg>
        044-555 010 200
      </li>
      <li>
        <svg viewBox="0 0 16 16"><circle cx="8" cy="8" r="8" fill="var(--orange)"/><rect x="4" y="5" width="8" height="6" fill="none" stroke="var(--black)" stroke-width="1.2"/><path d="M4 5l4 3.5L12 5" fill="none" stroke="var(--black)" stroke-width="1.2"/></svg>
        info@ridgewaymail.com
      </li>
      <li>
        <svg viewBox="0 0 16 16"><circle cx="8" cy="8" r="8" fill="var(--orange)"/><circle cx="8" cy="8" r="4.2" fill="none" stroke="var(--black)" stroke-width="1.1"/><path d="M3.8 8h8.4M8 3.8c-2 2.4-2 6 0 8.4M8 3.8c2 2.4 2 6 0 8.4" fill="none" stroke="var(--black)" stroke-width="1"/></svg>
        www.ridgewayhyd.com
      </li>
    </ul>

    <p class="address">Your Address, City<br>State, Zip 0000</p>
  </section>

</body>
</html>
```